Mabiboo creole shop needs a web design

We need a web design former new company based in sydney australia. Called 'Mabiboo, creole shop'.
We produce caribbean/west indies product alcohol, spirits, condiments, candies, preserved food, jams, pates.
We would like to see a design that reflect the caribbean without being tacky.
We want modern, high level design as we do high level products.

Reason: There is a lot of good proposition but I need a few more days to mature my decision. Thanks for your hard work Jorel

Industry/Entity Type

Hospitality

Number of Pages Required

1 page

Font styles to use
Decorative
Script

Requirements
Must have
• The logo, the name of the business

```html
<!DOCTYPE html>
<html lang="en">
<head>
<meta charset="utf-8">
<title>Mabiboo Creole Shop</title>
<link href="https://fonts.googleapis.com/css2?family=Dancing+Script:wght@700&family=Lato:wght@400;700&display=swap" rel="stylesheet">
<style>
:root{
  --gold:#d2a72e;
  --gold-light:#e0b93f;
  --navy:#1d2a5c;
  --ink:#222;
  --dark:#262626;
  --field:#5a5a5a;
  --white:#fff;
  --mist:#f2f2f2;
}
*{box-sizing:border-box;margin:0;padding:0}
html,body{width:798px;height:1200px;overflow:hidden;background:var(--white)}
body{font-family:"Lato",sans-serif;color:var(--ink);position:relative}
.abs{position:absolute}
.script{font-family:"Dancing Script",cursive;font-weight:700}

/* hero */
.hero-photo{left:0;top:0;width:798px;height:520px;
  background:
    radial-gradient(ellipse 180px 260px at 60px 180px,#5f8d2e 0%,rgba(95,141,46,.0) 100%),
    radial-gradient(ellipse 180px 220px at 760px 170px,#5f8d2e 0%,rgba(95,141,46,0) 100%),
    linear-gradient(180deg,#8f7a63 0%,#b59c7f 45%,#cdb89d 80%,#d8cbb8 100%);}
.topbar{left:0;top:0;width:798px;height:50px;color:var(--white);font-size:12px}
.topbar span{position:absolute;top:16px}
.social-dot{position:absolute;top:14px;width:20px;height:20px;border-radius:50%;background:var(--gold)}
.icon-dot{position:absolute;width:20px;height:20px;border-radius:50%;background:var(--gold);display:flex;align-items:center;justify-content:center}
.nav-band{left:0;top:50px;width:798px;height:36px;background:var(--white);border-top:2px solid var(--gold);border-bottom:2px solid var(--gold)}
.nav{left:181px;top:61px;width:562px;display:flex;justify-content:space-between;font-size:12.5px;color:var(--ink)}
.nav i{font-style:normal;color:var(--ink)}
.brand-badge{left:54px;top:14px;width:108px;height:108px;border-radius:50%;background:var(--white);border:2px solid var(--gold);display:flex;flex-direction:column;align-items:center;justify-content:center;color:var(--navy);font-size:20px;line-height:1.1;text-align:center}
.hero-badge{left:353px;top:182px;width:92px;height:92px;border-radius:50%;border:1.5px solid var(--white);display:flex;align-items:center;justify-content:center;color:var(--white);font-size:16px;text-align:center;line-height:1.15}
.hero-title{left:0;top:278px;width:798px;text-align:center;color:var(--white);font-size:46px}
.hero-sub{left:0;top:337px;width:798px;text-align:center;color:var(--white);font-size:20px}
.btn{background:var(--gold);color:var(--white);font-size:13px;border-radius:3px;display:flex;align-items:center;justify-content:center}

/* products */
.products-band{left:0;top:504px;width:798px;height:172px;background:var(--white)}
.about-band{left:0;top:676px;width:798px;height:248px;background:linear-gradient(180deg,#f7f7f7,#ececec)}
.product-photo{width:140px;height:140px;border-radius:50%;border:3px solid var(--white);box-shadow:0 0 0 1px #e6e6e6}
.product-inset{width:72px;height:72px;border-radius:50%;border:2px solid var(--gold)}
.product-name{width:176px;text-align:center;color:var(--gold);font-size:20px}
.product-text{width:176px;text-align:center;font-size:8.5px;line-height:13px;color:var(--ink)}
.arrow{top:512px;width:20px;height:36px}

/* about */
.about-title{left:0;top:690px;width:798px;text-align:center;font-size:38px}
.about-title .gold{color:var(--gold)}
.about-title .navy{color:var(--navy)}
.about-text{left:100px;top:755px;width:598px;text-align:center;font-size:8.5px;line-height:13.6px}

/* footer */
.footer{left:0;top:924px;width:798px;height:254px;background:var(--dark)}
.footer-badge{left:364px;top:892px;width:70px;height:70px;border-radius:50%;background:var(--dark);border:1.5px solid var(--white);display:flex;align-items:center;justify-content:center;color:var(--white);font-size:11px;text-align:center;line-height:1.15}
.f-head{top:976px;font-size:18px;color:var(--white)}
.f-head em{font-style:normal;color:var(--gold)}
.links{left:53px;top:1006px;list-style:none;color:var(--white);font-size:9.5px}
.links li{height:20.6px;display:flex;align-items:center}
.links li:before{content:"";width:4px;height:4px;border-radius:50%;background:var(--gold);margin-right:6px}
.contact{left:164px;top:1006px;color:var(--white);font-size:9.5px;line-height:13px}
.contact .row{position:absolute;left:0;display:flex;gap:6px;white-space:nowrap}
.contact .shop{color:var(--gold)}
.field{left:342px;width:142px;height:17px;background:var(--field);color:#ddd;font-size:8.5px;padding:3px 6px}
.submit{left:342px;top:1128px;width:142px;height:23px;background:var(--gold);color:var(--white);font-size:11px;font-weight:700;display:flex;align-items:center;justify-content:center}
.tile{width:50px;height:44px;border:1.5px solid var(--white)}
.follow{left:652px;color:var(--white);display:flex;align-items:center;gap:8px}
.follow .dot{width:24px;height:24px;border-radius:50%}
.follow b{display:block;font-size:9.5px}
.follow small{display:block;font-size:6px;color:#aaa}
.copyright{left:0;top:1178px;width:798px;height:22px;background:var(--gold);color:var(--ink);font-size:9px;display:flex;align-items:center;justify-content:center}
</style>
</head>
<body>

<div class="abs hero-photo" role="img" aria-label="Rum barrels stacked in an aged cellar framed by tropical palm fronds"></div>

<header class="abs topbar">
  <span style="left:272px">Follow Us:</span>
  <i class="social-dot" style="left:334px"></i>
  <i class="social-dot" style="left:364px"></i>
  <i class="social-dot" style="left:393px"></i>
  <i class="social-dot" style="left:423px"></i>
  <div class="icon-dot" style="left:475px;top:14px">
    <svg width="11" height="11" viewBox="0 0 24 24"><path fill="#fff" d="M6.6 10.8a15 15 0 0 0 6.6 6.6l2.2-2.2c.3-.3.7-.4 1-.2 1.1.4 2.3.6 3.6.6.6 0 1 .4 1 1V20c0 .6-.4 1-1 1A17 17 0 0 1 3 4c0-.6.4-1 1-1h3.5c.6 0 1 .4 1 1 0 1.3.2 2.5.6 3.6.1.3 0 .7-.2 1z"/></svg>
  </div>
  <span style="left:503px">info@mabiboo-shop.com</span>
  <div class="icon-dot" style="left:642px;top:14px">
    <svg width="11" height="9" viewBox="0 0 22 16"><rect x="1" y="1" width="20" height="14" fill="none" stroke="#fff" stroke-width="2"/><path d="M1 1l10 8 10-8" fill="none" stroke="#fff" stroke-width="2"/></svg>
  </div>
  <span style="left:668px;font-style:italic">123 456 7890</span>
</header>

<div class="abs nav-band"></div>
<nav class="abs nav">
  <span>Home</span><i>•</i><span>About Us</span><i>•</i><span>Our Services</span><i>•</i><span>Our Products</span><i>•</i><span>News &amp; Blog</span><i>•</i><span>Contact Us</span>
</nav>
<div class="abs brand-badge">Mabiboo<br>creole shop</div>

<div class="abs hero-badge">Mabiboo<br>creole shop</div>
<h1 class="abs hero-title script">We Manufacture</h1>
<p class="abs hero-sub">High Level Products</p>
<div class="abs btn" style="left:344px;top:376px;width:110px;height:30px">Get Started</div>

<div class="abs products-band"></div>
<div class="abs about-band"></div>

<svg class="abs arrow" style="left:14px" viewBox="0 0 20 36"><path d="M16 2L4 18l12 16" fill="none" stroke="#111" stroke-width="2.5"/></svg>
<svg class="abs arrow" style="left:764px" viewBox="0 0 20 36"><path d="M4 2l12 16L4 34" fill="none" stroke="#111" stroke-width="2.5"/></svg>

<div class="abs product-photo" style="left:76px;top:446px;background:radial-gradient(circle at 50% 40%,#4c4c3a,#1c1c16)" role="img" aria-label="Wine and rum bottles"></div>
<div class="abs product-inset" style="left:52px;top:516px;background:radial-gradient(circle,#3d3f63,#1d1f35)" role="img" aria-label="Dark grapes"></div>
<div class="abs product-photo" style="left:252px;top:446px;background:radial-gradient(circle at 50% 45%,#8c1d24,#4a0d12)" role="img" aria-label="Jar of strawberry jam"></div>
<div class="abs product-inset" style="left:228px;top:516px;background:radial-gradient(circle,#d8262c,#8c1014)" role="img" aria-label="Fresh strawberries"></div>
<div class="abs product-photo" style="left:428px;top:446px;background:radial-gradient(circle at 50% 50%,#f2a3cf,#d94ea0)" role="img" aria-label="Colourful hard candies"></div>
<div class="abs product-inset" style="left:404px;top:516px;background:radial-gradient(circle,#5a3a2a,#2a1a12)" role="img" aria-label="Chocolate covered beans"></div>
<div class="abs product-photo" style="left:604px;top:446px;background:radial-gradient(circle,#f4cc6e,#d9a23a)" role="img" aria-label="Dried farfalle pasta"></div>
<div class="abs product-inset" style="left:580px;top:516px;background:radial-gradient(circle,#efe6d6,#c9a97a)" role="img" aria-label="Sack of flour with wheat"></div>

<h3 class="abs product-name script" style="left:46px;top:594px">Alcohol</h3>
<p class="abs product-text" style="left:46px;top:625px">Lorem ipsum dolor sit amet,<br>feugait nulla facilisi.</p>
<h3 class="abs product-name script" style="left:222px;top:594px">Jams</h3>
<p class="abs product-text" style="left:222px;top:625px">Lorem ipsum dolor sit amet,<br>feugait nulla facilisi.</p>
<h3 class="abs product-name script" style="left:405px;top:594px">Spirits</h3>
<p class="abs product-text" style="left:405px;top:625px">Lorem ipsum dolor sit amet,<br>feugait nulla facilisi.</p>
<h3 class="abs product-name script" style="left:584px;top:594px">Condiments</h3>
<p class="abs product-text" style="left:584px;top:625px">Lorem ipsum dolor sit amet,<br>feugait nulla facilisi.</p>

<h2 class="abs about-title script"><span class="gold">About</span> <span class="navy">Mabiboo</span></h2>
<p class="abs about-text">Lorem ipsum dolor sit amet, consectetuer adipiscing elit, sed diam nonummy nibh euismod tincidunt ut laoreet dolore magna aliquam erat volutpat. Ut wisi enim ad minim veniam, quis nostrud exerci tation ullamcorper suscipit lobortis nisl ut aliquip ex ea commodo consequat. Duis autem vel eum iriure dolor in hendrerit in vulputate velit esse molestie consequat, vel illum dolore eu feugiat nulla facilisis at vero eros et accumsan et iusto odio dignissim qui blandit praesent luptatum zzril delenit augue duis dolore te feugait nulla facilisi.</p>
<div class="abs btn" style="left:354px;top:832px;width:96px;height:30px">Read All</div>

<footer class="abs footer"></footer>
<div class="abs footer-badge">Mabiboo<br>creole shop</div>

<h4 class="abs f-head script" style="left:53px">Quick <em>Links</em></h4>
<ul class="abs links">
  <li>Home</li><li>About Us</li><li>Our Services</li><li>Our Products</li><li>News &amp; Blog</li><li>Contact Us</li>
</ul>

<h4 class="abs f-head script" style="left:164px">Contact <em>Details</em></h4>
<div class="abs contact">
  <div class="row" style="top:0">
    <svg width="10" height="13" viewBox="0 0 10 14"><path d="M5 0a5 5 0 0 0-5 5c0 4 5 9 5 9s5-5 5-9a5 5 0 0 0-5-5z" fill="#d2a72e"/><circle cx="5" cy="5" r="1.8" fill="#262626"/></svg>
    <div><span class="shop">MABIBOO CREOLE SHOP</span><br>Street name,&nbsp; City Name,<br>Country-1234</div>
  </div>
  <div class="row" style="top:45px">
    <svg width="10" height="10" viewBox="0 0 24 24"><path fill="#d2a72e" d="M6.6 10.8a15 15 0 0 0 6.6 6.6l2.2-2.2c.3-.3.7-.4 1-.2 1.1.4 2.3.6 3.6.6.6 0 1 .4 1 1V20c0 .6-.4 1-1 1A17 17 0 0 1 3 4c0-.6.4-1 1-1h3.5c.6 0 1 .4 1 1 0 1.3.2 2.5.6 3.6.1.3 0 .7-.2 1z"/></svg>
    <span>123 456 7890</span>
  </div>
  <div class="row" style="top:70px">
    <svg width="12" height="10" viewBox="0 0 14 12"><rect x="1" y="3" width="12" height="4" rx="1" fill="#d2a72e"/><rect x="3" y="7" width="8" height="4" fill="none" stroke="#d2a72e" stroke-width="1.5"/></svg>
    <span>123 456 7890</span>
  </div>
  <div class="row" style="top:96px">
    <svg width="10" height="8" viewBox="0 0 22 16"><rect x="1" y="1" width="20" height="14" fill="#d2a72e"/><path d="M1 1l10 8 10-8" fill="none" stroke="#262626" stroke-width="2"/></svg>
    <span>hello@mabiboo-shop.com</span>
  </div>
</div>

<h4 class="abs f-head script" style="left:342px">Quick <em>Inquiry</em></h4>
<div class="abs field" style="top:1010px">Name</div>
<div class="abs field" style="top:1033px">E-mail</div>
<div class="abs field" style="top:1057px">Phone</div>
<div class="abs field" style="top:1082px;height:40px">Message</div>
<div class="abs submit">SUBMIT</div>

<h4 class="abs f-head script" style="left:514px">View <em>Gallery</em></h4>
<div class="abs tile" style="left:515px;top:1010px;background:#6b4a4a" role="img" aria-label="Barrel cellar"></div>
<div class="abs tile" style="left:570px;top:1010px;background:#2c2230" role="img" aria-label="Rum bottle"></div>
<div class="abs tile" style="left:515px;top:1058px;background:#3e5a3a" role="img" aria-label="Bottling line"></div>
<div class="abs tile" style="left:570px;top:1058px;background:#8a7a5a" role="img" aria-label="Preserve jars"></div>
<div class="abs tile" style="left:515px;top:1105px;background:#5a3a2a" role="img" aria-label="Production hall"></div>
<div class="abs tile" style="left:570px;top:1105px;background:#c9661e" role="img" aria-label="Jars of jam"></div>

<h4 class="abs f-head script" style="left:652px">Follow <em>Us</em></h4>
<div class="abs follow" style="top:1008px"><i class="dot" style="background:#2a9fd6"></i><div><b>CHIRPLINE</b><small>JOIN NOW</small></div></div>
<div class="abs follow" style="top:1038px"><i class="dot" style="background:#d6442f"></i><div><b>CIRCLENET</b><small>ADD TO CIRCLES</small></div></div>
<div class="abs follow" style="top:1069px"><i class="dot" style="background:#3a6d99"></i><div><b>SNAPFRAME</b><small>JOIN NOW</small></div></div>

<div class="abs copyright">Copyright 2015 Mabiboo Creole Shop. All Rights Reserved.</div>

</body>
</html>
```